Oven Cleaning Business owner needs business card design

Hi there,
Would like for a business card to be designed for myself, the owner of a professional oven cleaning business on the Sunshine Coast.
Would like it to look sleek, and modern-ish. Bit creative is encouraged too.
Include following:
Name/title: Corin ter Haghe, Owner
Phone number: 1300 482 916
Email: info@hearthshinecrew.com.au
Website: www.hearthshinecrew.com.au

```html
<!DOCTYPE html>
<html lang="en">
<head>
<meta charset="utf-8">
<title>Hearthshine Crew – Business Card</title>
<link rel="stylesheet" href="https://fonts.googleapis.com/css2?family=Figtree:wght@500;700;800&family=Montserrat:wght@400;500&display=swap">
<style>
  :root {
    --teal: #1ddde0;
    --foam-mid: #86d8e8;
    --foam-soft: #b9e8f1;
    --foam-pale: #e4f6fa;
    --white: #ffffff;
    --ink: #141414;
    --backdrop: #676767;
  }
  * { margin: 0; padding: 0; box-sizing: border-box; }
  html, body { width: 1200px; height: 924px; overflow: hidden; }
  body {
    background: var(--backdrop);
    font-family: "Figtree", sans-serif;
    position: relative;
  }
  .card {
    position: absolute;
    top: 302px;
    width: 560px;
    height: 320px;
    background: var(--white);
    overflow: hidden;
  }
  .card--front { left: 25px; }
  .card--back { left: 615px; }

  .foam-band {
    position: absolute; left: 0; right: 0;
    background: linear-gradient(180deg,
      var(--teal) 0%,
      var(--foam-mid) 30%,
      var(--foam-soft) 60%,
      var(--foam-pale) 85%,
      var(--white) 100%);
  }

  /* front */
  .front-field {
    position: absolute; inset: 0 0 auto 0; height: 170px;
    background: var(--teal);
  }
  .card--front .foam-band { top: 158px; height: 115px; }
  .brand-mark {
    position: absolute; left: 0; right: 0; top: 34px;
    display: flex; flex-direction: column; align-items: center; gap: 22px;
  }
  .brand-mark__dot {
    width: 96px; height: 96px; border-radius: 50%;
    background: var(--white);
  }
  .brand-mark__name {
    font-weight: 800; font-size: 30px; letter-spacing: 2px;
    color: var(--white); text-transform: uppercase;
  }
  .front-web {
    position: absolute; left: 0; right: 0; bottom: 24px;
    text-align: center;
    font-family: "Montserrat", sans-serif; font-size: 14px;
    letter-spacing: 2px; color: var(--ink);
  }

  /* back */
  .back-field {
    position: absolute; top: 0; right: 0; left: 190px; height: 175px;
    background: var(--teal);
  }
  .card--back .foam-band { top: 165px; height: 110px; left: 190px; }
  .hero-art {
    position: absolute; left: 8px; top: 34px;
    width: 262px; height: 262px; border-radius: 50%;
    background: var(--teal);
    border: 7px solid var(--white);
    box-shadow: 0 0 0 3px var(--teal);
  }
  .contact {
    position: absolute; left: 304px; top: 48px; color: var(--ink);
  }
  .contact__name { font-weight: 700; font-size: 18px; line-height: 1.1; }
  .contact__title { font-weight: 500; font-size: 15px; margin: 3px 0 7px; }
  .contact__list { list-style: none; }
  .contact__item {
    display: flex; align-items: center; gap: 7px;
    font-weight: 500; font-size: 11.5px; line-height: 20px;
  }
  .contact__icon { width: 11px; height: 11px; flex: none; }
  .back-brand {
    position: absolute; right: 40px; bottom: 30px;
    display: flex; align-items: center; gap: 10px;
  }
  .back-brand__dot {
    width: 32px; height: 32px; border-radius: 50%;
    background: var(--teal);
  }
  .back-brand__name {
    font-weight: 800; font-size: 19px; letter-spacing: 1px;
    color: var(--ink); text-transform: uppercase;
  }
</style>
</head>
<body>

<section class="card card--front">
  <div class="front-field"></div>
  <div class="foam-band" role="img" aria-label="Soap foam bubbles pattern"></div>
  <div class="brand-mark">
    <span class="brand-mark__dot"></span>
    <span class="brand-mark__name">Hearthshine Crew</span>
  </div>
  <p class="front-web">www.hearthshinecrew.com.au</p>
</section>

<section class="card card--back">
  <div class="back-field"></div>
  <div class="foam-band" role="img" aria-label="Soap foam bubbles pattern"></div>
  <div class="hero-art" role="img" aria-label="Large water drop illustration with a clean oven and sparkles"></div>

  <div class="contact">
    <p class="contact__name">Corin ter Haghe,</p>
    <p class="contact__title">OWNER</p>
    <ul class="contact__list">
      <li class="contact__item">
        <svg class="contact__icon" viewBox="0 0 12 12"><circle cx="6" cy="6" r="6" fill="#141414"/><path d="M4 3.2l1 1.4-.6.7c.4.8 1 1.4 1.8 1.8l.7-.6 1.4 1-.6 1.2C5.5 8.5 3.5 6.5 3.3 3.8z" fill="#fff"/></svg>
        1300 482 916
      </li>
      <li class="contact__item">
        <svg class="contact__icon" viewBox="0 0 12 12"><circle cx="6" cy="6" r="6" fill="#141414"/><rect x="3" y="4" width="6" height="4.2" fill="none" stroke="#fff" stroke-width=".8"/><path d="M3 4l3 2.3L9 4" fill="none" stroke="#fff" stroke-width=".8"/></svg>
        info@hearthshinecrew.com.au
      </li>
      <li class="contact__item">
        <svg class="contact__icon" viewBox="0 0 12 12"><circle cx="6" cy="6" r="6" fill="#141414"/><circle cx="6" cy="6" r="3.2" fill="none" stroke="#fff" stroke-width=".7"/><ellipse cx="6" cy="6" rx="1.3" ry="3.2" fill="none" stroke="#fff" stroke-width=".7"/><path d="M2.8 6h6.4" stroke="#fff" stroke-width=".7"/></svg>
        www.hearthshinecrew.com.au
      </li>
    </ul>
  </div>

  <div class="back-brand">
    <span class="back-brand__dot"></span>
    <span class="back-brand__name">Hearthshine Crew</span>
  </div>
</section>

</body>
</html>
```